CopperWren Works, LLC Corporate Web Site

The goal of this web site is simple. To provide an information and corporate information site for people who click on company links from other web sites. Put simply, this web site is primarily a brochure web site for the parent business. It will contain information about the company and our products with links to those products. It will be designed as a small web site but scalable as we add more products and services to our repertoire.

Please see the PDF in the uploaded files/media for more information on colors and basic guidelines, but be creative for sure.

Target Market(s)

General

Industry/Entity Type

Technology, Software

Coding

Coded - Design and coding required

Font styles to use
Other font styles liked:
• Goliath, Roboto

Colors
FFC000
F8CF3A
FAE287
FDF2CF
FEFAEE

Requirements
Must have
• Home page template, interior template, News/Press release template
Nice to have
• Searchable
Should not have
• carousels, one-page design

```html
<!DOCTYPE html>
<html lang="en">
<head>
<meta charset="utf-8">
<title>CopperWren Works — Projects</title>
<link href="https://fonts.googleapis.com/css2?family=Bubblegum+Sans&family=Figtree:wght@400;500;600;700&display=swap" rel="stylesheet">
<style>
:root{
  --navy:#07162e;
  --orange:#f7941d;
  --orange-light:#f9a23a;
  --peach:#fdf1e0;
  --ink:#111111;
  --text:#2b2b2b;
  --muted:#555;
  --rule:#c9c9c9;
  --white:#ffffff;
}
*{margin:0;padding:0;box-sizing:border-box}
html,body{width:1200px;height:3087px;overflow:hidden}
body{position:relative;background:var(--white);font-family:"Figtree",Arial,sans-serif;color:var(--text)}
.display{font-family:"Bubblegum Sans","Comic Sans MS",cursive;letter-spacing:1px}

/* header */
.site-header{position:absolute;left:0;top:0;width:1200px;height:82px;background:var(--navy)}
.brand{position:absolute;left:162px;top:18px;display:flex;align-items:center;gap:10px;color:var(--orange);font-weight:700;font-size:26px}
.brand-dot{width:14px;height:14px;border-radius:50%;background:var(--orange)}
.main-nav{position:absolute;left:469px;top:26px;display:flex;gap:37px}
.main-nav a{color:var(--white);font-size:13.5px;text-decoration:none;font-weight:500}
.main-nav a.active{color:var(--orange);font-weight:700}

/* hero */
.hero-glow{position:absolute;left:540px;top:-560px;width:1060px;height:900px;border-radius:50%;background:var(--peach)}
.hero-title{position:absolute;left:162px;top:180px}
.hero-title .lead{font-size:36px;color:#333;font-weight:400}
.hero-title h1{font-size:50px;color:var(--orange);font-weight:400;line-height:1;margin-top:2px}
.breadcrumb{position:absolute;left:162px;top:283px;font-size:13px;color:#333}
.breadcrumb span{color:var(--orange)}
.hero-art{position:absolute;left:672px;top:138px;width:306px;height:276px;border-radius:50% 50% 48% 48%;background:radial-gradient(ellipse at 50% 60%,#3a4756 0%,#4d5b6a 35%,#e8e8ea 70%,#f3efe9 100%)}

/* sections */
.section-title{position:absolute;left:0;width:1200px;text-align:center;font-size:48px;color:var(--ink);font-weight:400}
.section-lead{position:absolute;left:300px;width:600px;text-align:center;font-size:13px;line-height:24.5px;color:#222}

.card-grid{position:absolute;left:162px;width:877px;display:grid;grid-template-columns:repeat(3,280px);column-gap:18px;row-gap:23px}
.card{height:521px;position:relative}
.card-media{height:322px;border-radius:7px}
.card-body{border-left:1px solid var(--rule);margin-left:2px;height:199px;padding:20px 0 0 19px}
.card-title{font-size:14.5px;font-weight:700;color:var(--ink);line-height:24px}
.card-text{font-size:12.8px;line-height:24.5px;color:#333;margin-top:8px;width:258px}
.card-link{display:inline-block;margin-top:6px;font-size:12.8px;font-weight:700;color:var(--orange);text-decoration:underline}

.m-software{background:linear-gradient(150deg,#e8b15a 0%,#d8d7d2 40%,#a9c4e6 70%,#6f93c9 100%)}
.m-saas{background:linear-gradient(160deg,#1d2027 0%,#4b4f58 50%,#1b1f27 100%)}
.m-secure{background:linear-gradient(140deg,#3a3c40 0%,#2c6f9c 55%,#5fb8e6 100%)}
.m-code{background:linear-gradient(150deg,#0f1b2d 0%,#1e3b66 50%,#0b1524 100%)}
.m-team{background:linear-gradient(160deg,#8e8e8e 0%,#c9b8a4 45%,#5a5550 100%)}
.m-dev{background:linear-gradient(160deg,#d9dcde 0%,#b7bcc0 45%,#5f5a55 100%)}

.btn{position:absolute;left:525px;width:150px;height:45px;border-radius:23px;background:var(--orange);color:var(--white);font-weight:700;font-size:14px;display:flex;align-items:center;justify-content:center;text-decoration:none}

/* footer */
.site-footer{position:absolute;left:0;top:2650px;width:1200px;height:437px}
.footer-bg{position:absolute;left:0;top:0}
.footer-heading{position:absolute;font-size:20px;color:var(--white);font-weight:400}
.quick-links{position:absolute;left:163px;top:183px;list-style:none}
.quick-links li{font-size:13px;line-height:30px;color:var(--white)}
.footer-brand{position:absolute;left:400px;top:180px;width:232px;text-align:center;color:var(--white);font-weight:700;font-size:28px}
.social{position:absolute;left:473px;top:261px;display:flex;gap:11px}
.social span{width:38px;height:38px;border:1.5px solid var(--white);border-radius:50%}
.contact{position:absolute;left:776px;top:186px}
.contact-item{display:flex;align-items:center;gap:18px;height:44px;margin-bottom:17px;color:var(--white);font-size:13px;line-height:21px}
.contact-item svg{flex:none}
.contact-item strong{font-weight:700}
.footer-rule{position:absolute;left:162px;top:376px;width:877px;height:1px;background:#3a4659}
.copyright{position:absolute;left:0;top:401px;width:1200px;text-align:center;color:var(--white);font-size:12.5px}
.copyright b{color:var(--orange);font-weight:700}
</style>
</head>
<body>

<div class="hero-glow"></div>

<header class="site-header">
  <div class="brand"><span class="brand-dot"></span>CopperWren Works</div>
  <nav class="main-nav">
    <a href="#">Home</a><a href="#">About</a><a href="#">Products</a><a href="#" class="active">Projects</a><a href="#">Contributions</a><a href="#">News</a><a href="#">Privacy</a>
  </nav>
</header>

<div class="hero-title">
  <p class="lead">Our</p>
  <h1 class="display">PROJECTS</h1>
</div>
<p class="breadcrumb">Home &#187; <span>Projects</span></p>
<div class="hero-art" role="img" aria-label="Illustration of two people with giant pencils beside a business plan board with charts"></div>

<h2 class="section-title display" style="top:490px">CURRENT PROJECTS</h2>
<p class="section-lead" style="top:548px">Lorem ipsum dolor sit amet, consectetur adipiscing elit. Aliquam at aliquam augue, vitae auctor quam. Ut eleifend lacus sem, nec dictum leo placerat quis.</p>

<div class="card-grid" style="top:637px">
  <article class="card"><div class="card-media m-software" role="img" aria-label="Tablet showing software and database screens"></div><div class="card-body"><h3 class="card-title">Lorem Ipsum Dolor Sit Amet Consectetur Adipiscing Elit.</h3><p class="card-text">Lorem ipsum dolor sit amet, consectetur adipiscing elit. Aliquam at aliquam augue auctor quam. Ut eleifend lacus sem, nec dictum leo placerat quis.</p><a class="card-link" href="#">View Details</a></div></article>
  <article class="card"><div class="card-media m-saas" role="img" aria-label="Hands on a tablet with SaaS cloud diagram"></div><div class="card-body"><h3 class="card-title">Lorem Ipsum Dolor Sit Amet Consectetur Adipiscing Elit.</h3><p class="card-text">Lorem ipsum dolor sit amet, consectetur adipiscing elit. Aliquam at aliquam augue auctor quam. Ut eleifend lacus sem, nec dictum leo placerat quis.</p><a class="card-link" href="#">View Details</a></div></article>
  <article class="card"><div class="card-media m-secure" role="img" aria-label="Hand touching a tablet with glowing check and gear icons"></div><div class="card-body"><h3 class="card-title">Lorem Ipsum Dolor Sit Amet Consectetur Adipiscing Elit.</h3><p class="card-text">Lorem ipsum dolor sit amet, consectetur adipiscing elit. Aliquam at aliquam augue auctor quam. Ut eleifend lacus sem, nec dictum leo placerat quis.</p><a class="card-link" href="#">View Details</a></div></article>
  <article class="card"><div class="card-media m-code" role="img" aria-label="Laptop keyboard with floating HTML code graphics"></div><div class="card-body"><h3 class="card-title">Lorem Ipsum Dolor Sit Amet Consectetur Adipiscing Elit.</h3><p class="card-text">Lorem ipsum dolor sit amet, consectetur adipiscing elit. Aliquam at aliquam augue auctor quam. Ut eleifend lacus sem, nec dictum leo placerat quis.</p><a class="card-link" href="#">View Details</a></div></article>
  <article class="card"><div class="card-media m-team" role="img" aria-label="Team meeting around a laptop with coffee cups"></div><div class="card-body"><h3 class="card-title">Lorem Ipsum Dolor Sit Amet Consectetur Adipiscing Elit.</h3><p class="card-text">Lorem ipsum dolor sit amet, consectetur adipiscing elit. Aliquam at aliquam augue auctor quam. Ut eleifend lacus sem, nec dictum leo placerat quis.</p><a class="card-link" href="#">View Details</a></div></article>
  <article class="card"><div class="card-media m-dev" role="img" aria-label="Hands typing on a laptop showing a development flow chart"></div><div class="card-body"><h3 class="card-title">Lorem Ipsum Dolor Sit Amet Consectetur Adipiscing Elit.</h3><p class="card-text">Lorem ipsum dolor sit amet, consectetur adipiscing elit. Aliquam at aliquam augue auctor quam. Ut eleifend lacus sem, nec dictum leo placerat quis.</p><a class="card-link" href="#">View Details</a></div></article>
</div>

<a class="btn" href="#" style="top:1748px">View All</a>

<h2 class="section-title display" style="top:1867px">OUR BEST PROJECTS</h2>

<div class="card-grid" style="top:1958px">
  <article class="card"><div class="card-media m-software" role="img" aria-label="Tablet showing software and database screens"></div><div class="card-body"><h3 class="card-title">Lorem Ipsum Dolor Sit Amet Consectetur Adipiscing Elit.</h3><p class="card-text">Lorem ipsum dolor sit amet, consectetur adipiscing elit. Aliquam at aliquam augue auctor quam. Ut eleifend lacus sem, nec dictum leo placerat quis.</p><a class="card-link" href="#">View Details</a></div></article>
  <article class="card"><div class="card-media m-team" role="img" aria-label="Team meeting around a laptop with coffee cups"></div><div class="card-body"><h3 class="card-title">Lorem Ipsum Dolor Sit Amet Consectetur Adipiscing Elit.</h3><p class="card-text">Lorem ipsum dolor sit amet, consectetur adipiscing elit. Aliquam at aliquam augue auctor quam. Ut eleifend lacus sem, nec dictum leo placerat quis.</p><a class="card-link" href="#">View Details</a></div></article>
  <article class="card"><div class="card-media m-secure" role="img" aria-label="Hand touching a tablet with glowing check and gear icons"></div><div class="card-body"><h3 class="card-title">Lorem Ipsum Dolor Sit Amet Consectetur Adipiscing Elit.</h3><p class="card-text">Lorem ipsum dolor sit amet, consectetur adipiscing elit. Aliquam at aliquam augue auctor quam. Ut eleifend lacus sem, nec dictum leo placerat quis.</p><a class="card-link" href="#">View Details</a></div></article>
</div>

<a class="btn" href="#" style="top:2525px">View All</a>

<footer class="site-footer">
  <svg class="footer-bg" width="1200" height="437" viewBox="0 0 1200 437" aria-hidden="true">
    <path d="M0,150 Q600,-120 1200,150 L1200,437 L0,437 Z" fill="var(--navy)"/>
    <path d="M0,150 Q600,-120 1200,150" fill="none" stroke="var(--orange)" stroke-width="4"/>
  </svg>

  <h4 class="footer-heading display" style="left:163px;top:127px">QUICK LINKS</h4>
  <ul class="quick-links">
    <li>Home</li><li>About</li><li>Products</li><li>Projects</li><li>Contributions</li><li>News</li>
  </ul>

  <div class="footer-brand">CopperWren Works</div>
  <div class="social" aria-label="Social profiles"><span></span><span></span></div>

  <h4 class="footer-heading display" style="left:777px;top:136px">CONTACT DETAILS</h4>
  <div class="contact">
    <div class="contact-item">
      <svg width="44" height="44" viewBox="0 0 44 44" aria-hidden="true"><circle cx="22" cy="22" r="21" fill="none" stroke="#fff" stroke-width="1.5"/><path d="M22 13a6 6 0 0 0-6 6c0 5 6 12 6 12s6-7 6-12a6 6 0 0 0-6-6z" fill="#fff"/><circle cx="22" cy="19" r="2.2" fill="var(--navy)"/></svg>
      <div>123, Building Name, Street<br>City, State XY 123456</div>
    </div>
    <div class="contact-item">
      <svg width="44" height="44" viewBox="0 0 44 44" aria-hidden="true"><circle cx="22" cy="22" r="21" fill="none" stroke="#fff" stroke-width="1.5"/><path d="M16 14c1-1 2.5-1 3 .3l1.5 3.2c.4.9 0 1.7-.7 2.2l-1 .8c1 2.2 2.6 3.8 4.8 4.8l.8-1c.5-.7 1.3-1.1 2.2-.7l3.2 1.5c1.3.5 1.3 2 .3 3l-1.3 1.3c-1.4 1.4-8 0-12-4s-5.4-10.6-4-12z" fill="#fff"/></svg>
      <div><strong>Call Us</strong><br>123-456-7890</div>
    </div>
    <div class="contact-item">
      <svg width="44" height="44" viewBox="0 0 44 44" aria-hidden="true"><circle cx="22" cy="22" r="21" fill="none" stroke="#fff" stroke-width="1.5"/><rect x="13" y="16" width="18" height="13" rx="1.5" fill="none" stroke="#fff" stroke-width="1.8"/><path d="M13.5 17l8.5 6.5 8.5-6.5" fill="none" stroke="#fff" stroke-width="1.8"/></svg>
      <div><strong>Email</strong><br>info@copperwrenworks.com</div>
    </div>
  </div>

  <div class="footer-rule"></div>
  <p class="copyright">© 2023 <b>CopperWren Works</b>. All Rights Reserved. &nbsp;!&nbsp; Privacy Policy</p>
</footer>

</body>
</html>
```